Pagevoより「最前線・空腹がすっと静まる献立&噛み方の手引き」というタイトルの電子書籍を出版予定です。

この本のコンセプトは「食べ物を選んで食べること&その食べ方で食欲が自然におさまること、更にはそれがダイエットと健康維持とアンチエイジングに非常に効果的であること、プラス今流行りのダイエット方(オートファジーダイエット、ミトコンドリア活性化、ケトジェニックダイエット、16時間断食、レクチンフリー 食品の勧め、腸活、SATエクササイズ、オイルの種類など)の説明とご提案(やり方)」をお伝えし、読者の皆様の健康維持に貢献したいということです。

ターゲットは男女ともに考えております。デザインは明るくて「何これ、ダイエットや食品の本にしては発想が新しい!」と興味を持ってもらえることを期待しております。(抽象的ですみません;)

何かご質問・ご提案がありましたらいつでもご連絡ください。
どうぞ宜しくお願いいたします。
*以下2項目の追加記載をお願いいたします。お手数ですがどうぞ宜しくお願いいたします。

・読者プレゼント
星座タイプ別 きみに向く減量術と献立チェック

・著者名: 森川 結奈
皆様、お忙しいところをたくさんのご応募、ありがとうございました!
どれも素敵なデザインでなかなか決めるのが難しいところではありますが、
数日中に決定、上位3名の方にご連絡いたします。

それでは、どうぞしばらくお待ちくださいませ。

取り急ぎ、お礼まで。

Thank you so much!
森川 結奈

当選:miru72_studio様 ー 明るくてフレッシュで清潔感のあるイメージで、何だろう?と書店だったら思わず手に取りたくなる素敵なデザインだと思いました。 次点:ripple_308様 ー デザインが可愛いく親しみやすいのと「食事を抑えるのでなく食欲を抑えるダイエット」など刺さるコピーがとても鋭いと感じました。執筆仲間にも好評でした。 次点: Hnbrook様 ー シンプルで見やすいが故に、逆に何が書いてあるんだろう?と興味を持たせてくれそうなデザインだと感じました。仲間内でも好評でした。

選定が遅くなり大変申し訳ございませんでした。この度は沢山の素敵なデザインをご提案くださり、ありがとうございました。 周りの者と相談の上、悩んだ末に決定させていただきました。 本当に素晴らしい作品ばかりで、デザインをするお仕事の素晴らしさを教えていただきました。 皆様のパワーにインスパイアされ、また二冊目も書きたいと思う原動力をいただきました。 またぜひご縁をいただけたら幸いです。 心より感謝申し上げます。どうもありがとうございました。 皆様のますますのご活躍とご発展をお祈り申し上げます。森川結奈

```html
<!DOCTYPE html>
<html lang="ja">
<head>
<meta charset="utf-8">
<title>最前線・空腹がすっと静まる献立&噛み方の手引き</title>
<link rel="stylesheet" href="https://fonts.googleapis.com/css2?family=M+PLUS+Rounded+1c:wght@500;700;800&display=swap">
<style>
  :root {
    --ink-green: #2f4a26;
    --leaf-green: #4e8a2e;
    --band-green: #2d4620;
    --badge-yellow: #f6c21a;
    --badge-red: #d8321e;
    --panel: rgba(255, 255, 255, 0.93);
    --white: #ffffff;
    --title-ink: #333d2b;
  }
  * { margin: 0; padding: 0; box-sizing: border-box; }
  html, body { width: 750px; height: 1200px; overflow: hidden; background: #ffffff; }
  body { font-family: "M PLUS Rounded 1c", sans-serif; }
  .cover { position: relative; width: 750px; height: 1200px; overflow: hidden; }
  .cover-photo {
    position: absolute; inset: 0;
    background:
      radial-gradient(circle at 88% 62%, #b2556e 0 70px, transparent 150px),
      radial-gradient(circle at 70% 88%, #cfa0b0 0 40px, transparent 120px),
      radial-gradient(circle at 12% 58%, #6f9b50 0, transparent 220px),
      linear-gradient(160deg, #5f7c3a 0%, #3f6a2c 35%, #7fa65a 60%, #4f7a38 80%, #7a6a55 100%);
  }
  .title-panel {
    position: absolute; left: 25px; top: 12px; width: 700px; height: 500px;
    background: var(--panel); border-radius: 26px;
  }
  .kicker { position: absolute; left: 70px; top: 70px; display: flex; align-items: center; }
  .kicker-badge {
    width: 68px; height: 68px; border-radius: 50%; background: var(--badge-yellow);
    color: var(--badge-red); font-weight: 800; font-size: 44px;
    display: flex; align-items: center; justify-content: center;
  }
  .kicker-text { margin-left: 6px; color: var(--leaf-green); font-weight: 800; font-size: 50px; }
  .title-line { position: absolute; left: 70px; color: var(--title-ink); font-weight: 800; letter-spacing: 1px; white-space: nowrap; line-height: 1.2; }
  .title-line.one { top: 150px; font-size: 48px; }
  .title-line.two { top: 210px; font-size: 48px; }
  .title-line .small { font-size: 36px; }
  .title-main {
    position: absolute; left: 68px; top: 290px; color: var(--ink-green);
    font-weight: 800; font-size: 112px; letter-spacing: 18px; line-height: 1;
  }
  .title-rule { position: absolute; left: 70px; top: 418px; width: 420px; height: 3px; background: #b9d48a; }
  .author { position: absolute; left: 70px; top: 428px; color: var(--title-ink); font-weight: 700; font-size: 36px; }
  .farm-art {
    position: absolute; left: 505px; top: 255px; width: 150px; height: 210px;
    border-radius: 20px; background: linear-gradient(180deg, #cfe3b4, #f0d79a);
  }
  .points { position: absolute; left: 40px; top: 588px; list-style: none; }
  .points li {
    color: var(--white); font-weight: 700; font-size: 28px; line-height: 45px;
    text-shadow: 0 1px 4px rgba(0,0,0,0.55);
  }
  .gift-band { position: absolute; left: 0; top: 982px; width: 750px; height: 218px; background: var(--band-green); }
  .gift-label {
    position: absolute; left: 372px; top: 22px; color: var(--white); white-space: nowrap;
    font-weight: 700; font-size: 26px; padding: 4px 12px;
    border-left: 3px solid var(--white); border-right: 3px solid var(--white); border-radius: 6px;
    transform: rotate(-4deg);
  }
  .gift-icon { position: absolute; left: 596px; top: 18px; width: 50px; height: 50px; }
  .gift-sub { position: absolute; left: 38px; top: 74px; color: var(--white); font-weight: 700; font-size: 32px; white-space: nowrap; }
  .gift-main { position: absolute; left: 38px; top: 130px; color: var(--white); font-weight: 800; font-size: 40px; white-space: nowrap; }
</style>
</head>
<body>
<main class="cover">
  <div class="cover-photo" role="img" aria-label="新鮮な野菜の写真（葉物、紫玉ねぎ、かぶ、ねぎなど）"></div>

  <section class="title-panel">
    <div class="kicker"><span class="kicker-badge">最</span><span class="kicker-text">前線</span></div>
    <h1>
      <span class="title-line one">空腹がすっと静まる</span>
      <span class="title-line two">献立&amp;噛み方<span class="small">の</span></span>
      <span class="title-main">手引き</span>
    </h1>
    <div class="title-rule"></div>
    <p class="author">森川 結奈 著</p>
    <div class="farm-art" role="img" aria-label="野菜を運ぶ農家の二人のイラスト"></div>
  </section>

  <ul class="points">
    <li>食べ物を選んで食べること</li>
    <li>食べ方で食欲が自然におさまる</li>
    <li>ダイエットと健康維持とアンチエイジング</li>
    <li>今流行りのダイエット方法の説明と提案</li>
  </ul>

  <section class="gift-band">
    <span class="gift-label">読者プレゼント</span>
    <svg class="gift-icon" viewBox="0 0 52 52" aria-hidden="true">
      <rect x="8" y="20" width="36" height="28" rx="2" fill="none" stroke="#fff" stroke-width="3"/>
      <rect x="5" y="13" width="42" height="9" rx="2" fill="none" stroke="#fff" stroke-width="3"/>
      <line x1="26" y1="13" x2="26" y2="48" stroke="#fff" stroke-width="3"/>
      <path d="M26 13 C18 2, 10 8, 18 13 M26 13 C34 2, 42 8, 34 13" fill="none" stroke="#fff" stroke-width="3"/>
    </svg>
    <p class="gift-sub">星座タイプ別</p>
    <p class="gift-main">きみに向く減量術と献立チェック</p>
  </section>
</main>
</body>
</html>
```